Local primary school needs a flyer design for their fundraising fete

I need a flyer design for a local primary school holding a fundraising fete. I would like to see designs that feature the school logo, school colours (red white and navy) and that reference/mention the main rides and stalls at the event. If possible I would like the sponsors (on the newsletter supplied) to be included and the photo of the school available on the website. The final design should be easy for me to print and produce myself so that can leave at local shops, cafes etc. leading up to the event.

School

Font styles to use
Serif

Colors
ec2027
ffffff

```html
<!DOCTYPE html>
<html lang="en">
<head>
<meta charset="utf-8">
<title>School Fete Flyer</title>
<link rel="stylesheet" href="https://fonts.googleapis.com/css2?family=Oranienbaum&family=Cabin:wght@400;600;700&display=swap">
<style>
:root{
  --navy:#1d3f93;
  --navy-dark:#1b2f7a;
  --red:#c8102e;
  --red-band:#c41230;
  --white:#ffffff;
  --faint:#f6dcd2;
  --text-blue:#1f3f95;
}
*{margin:0;padding:0;box-sizing:border-box}
html,body{width:1200px;height:2544px;overflow:hidden;background:var(--white)}
body{font-family:'Cabin',sans-serif;position:relative}
.flyer{
  position:absolute;left:85px;top:80px;width:1030px;height:2392px;
  border:8px solid var(--navy);border-radius:34px;overflow:hidden;background:var(--white);
}
.header{background:var(--navy);height:484px;text-align:center;color:var(--white);padding-top:12px}
.header h1{font-family:'Oranienbaum',serif;font-weight:400;font-size:196px;line-height:200px;display:inline-block;transform:scaleY(1.3);transform-origin:center top}
.header .school{font-weight:700;font-size:47px;line-height:57px;margin-top:52px;letter-spacing:2px}
.header .lead{font-weight:700;font-size:45px;line-height:54px}
.date-band{background:var(--red-band);height:185px;color:var(--white);text-align:center;font-weight:700;font-size:76px;line-height:72px;padding-top:22px}
.photo{height:176px;position:relative;background:linear-gradient(90deg,#b9c6d4 0%,#8fa0b3 40%,#c9d3dc 75%,#8c9aa8 100%)}
.photo .caption{position:absolute;left:236px;top:36px;color:var(--white);font-size:38px;line-height:42px;font-weight:600}
.photo .caption small{display:block;font-size:26px;font-weight:400}
.photo .crest{position:absolute;left:20px;top:18px;width:140px;height:140px;background:var(--white);border-radius:50%}
.body{position:relative;padding:38px 50px 0 68px;color:var(--text-blue)}
.watermark{position:absolute;left:200px;top:40px;width:700px;height:700px;border-radius:50%;background:var(--faint);opacity:.55}
.body p{position:relative}
.intro{font-size:38px;line-height:50px}
.big{color:var(--red);font-weight:700;font-size:92px;line-height:90px;white-space:nowrap}
.big.one{margin-top:26px}
.big.two{padding-left:105px}
.game{font-size:38px;line-height:50px;padding-left:200px;margin-top:2px}
.big.three{padding-left:165px;margin-top:15px}
.para{font-size:40px;line-height:57px;margin-top:49px;white-space:nowrap}
.para b{color:var(--red);font-weight:700}
.para + .para{margin-top:24px}
.rule{position:absolute;left:10px;right:10px;top:1873px;height:5px;background:var(--navy)}
.sponsors{position:absolute;left:0;right:0;top:1905px;text-align:center}
.sponsors h2{font-weight:400;color:var(--text-blue);font-size:40px;line-height:50px;letter-spacing:1px}
.sponsor-grid{display:flex;flex-wrap:wrap;justify-content:center;gap:8px 26px;padding:22px 30px 0}
.sponsor{font-weight:700;font-size:34px;line-height:56px;color:var(--navy-dark)}
.sponsor.red{color:var(--red)}
</style>
</head>
<body>
<div class="flyer">
  <header class="header">
    <h1>School Fete</h1>
    <p class="school">ST BRIGID'S PRIMARY SCHOOL<br>14 WATTLE STREET, FERNDALE</p>
    <p class="lead">will hold their biannual fete on</p>
  </header>
  <div class="date-band">Sunday 21 September<br>from 11am to 3pm</div>
  <div class="photo" role="img" aria-label="Photo of the school building">
    <div class="crest"></div>
    <p class="caption">St Brigid's Primary School<small>Ferndale, Hillsbury</small></p>
  </div>
  <main class="body">
    <div class="watermark"></div>
    <p class="intro">There will be some fantastic rides, including</p>
    <p class="big one">jumping castles</p>
    <p class="big two">horizontal bungy</p>
    <p class="game">and if you’re game, even a</p>
    <p class="big three">wild bucking bull!</p>
    <p class="para">There will also be the old fete favourites,<br>including the <b>petting zoo</b>, <b>arts and craft</b>,<br>the <b>chocolate wheel</b> and the <b>cake stall</b><br>to name a few along with other wonderful<br>treats and delicious food to eat. With over 20<br>stalls, there will be something for everyone.</p>
    <p class="para">So come along for a <b>family</b> excursion filled<br>with <b>fun</b> and some <b>bargain buys</b> too...</p>
  </main>
  <div class="rule"></div>
  <section class="sponsors">
    <h2>OUR SPONSORS</h2>
    <div class="sponsor-grid">
      <span class="sponsor">Harlow Plumbing</span>
      <span class="sponsor">Keystone Realty</span>
      <span class="sponsor">Bellvale Motors</span>
      <span class="sponsor">CodeLeaf</span>
      <span class="sponsor">Olive Club</span>
      <span class="sponsor">Brightway Dental</span>
      <span class="sponsor">Smile Align</span>
      <span class="sponsor">Lumo Hair</span>
      <span class="sponsor red">Scoop Corner</span>
      <span class="sponsor">Velour</span>
      <span class="sponsor">Tarrow Group</span>
      <span class="sponsor red">Stride Sports</span>
      <span class="sponsor red">Timber Deck Co</span>
      <span class="sponsor">Norvane</span>
      <span class="sponsor">Riverstage Arts</span>
      <span class="sponsor red">Gift Hamper Co</span>
      <span class="sponsor">Wander Travel</span>
    </div>
  </section>
</div>
</body>
</html>
```